Visitenkarten-Design für Hausarztpraxis
Zielgruppe
Hausarztpraxis mit Schwerpunkt Geriatrie
Zielgruppe: Patienten in einem eher ländlichen Stadtgebiet mit hoher Anzahl von Senioren
Aufgabenstellung
Idee: Kombination eines Gutscheines für eine Kaffespezialität auf der Rückseite und einer beschreibbaren Vorderseite als Bestellkärtchen mit Foto von zukünftigen "Praxisgängern" im Querschnitt. D.h. Zu sehen sein sollten 1 lustige Oma , 1 lustiger Opa (z.B. Pfeife rauchend), 1 Jugendlicher und diverse andere Erwachsene verschiedener Berufsgruppen. Beispielhaft siehe unter: Tintenfuchs: Online Terminvereinbarung-Die keine Wünsche offen lässt. Das Bild könnte auch "gezeichnet" sein. Ich würde aber ein treffendes Foto bevorzugen. Design: gut leserliche Schrift, keine verschlungene Schriftarten, wegen Lesbarkeit für Renterklientel.
Info auf der Vorderseite mit Foto: WARTEN? Nicht bei uns - Ihr persönlicher Wunschtermin:
Info auf der Rückseite (Gutschein): Gutschein für eine Kaffeespezialität (Kaffeesymbol)
farblich unterlegt, Farbe egal, passend abgestimmt zur Vorderseite
Zur Erklärung:
Die Form/ Grösse sollte die einer Visitenkarte möglichst nicht überschreiten. Gern auch eine grössere Visitenkartenform 10cm breit und 7,5 cm hoch. Das Format ist unserem Zeitdruck geschuldet. Es muss ein Werbemittel in 14 Tagen zur Praxiseröffnung zur Verfügung stehen, was sich schnell und kostengünstig produzieren und bei Bedarf ohne Probleme nachproduzieren lässt.
Sonderformate haben lange Auftragszeiten bei den auszuführenden Werbedruckfirmen.

```html
<!DOCTYPE html>
<html lang="de">
<head>
<meta charset="utf-8">
<title>Visitenkarten Hausarztpraxis</title>
<link href="https://fonts.googleapis.com/css2?family=Questrial&display=swap" rel="stylesheet">
<style>
  :root {
    --praxis-blau: #1d4e69;
    --weiss: #ffffff;
    --hintergrund: #ffffff;
  }
  html, body {
    margin: 0;
    padding: 0;
    width: 1200px;
    height: 1200px;
    overflow: hidden;
    background: var(--hintergrund);
    font-family: "Questrial", "Century Gothic", sans-serif;
  }
  .card {
    position: absolute;
    left: 233px;
    width: 741px;
    height: 480px;
    overflow: hidden;
  }
  .card--front { top: 52px; background: var(--weiss); }
  .card--back { top: 599px; background: var(--praxis-blau); }
  .card svg.card-shapes {
    position: absolute;
    inset: 0;
    width: 741px;
    height: 480px;
  }
  .text {
    position: absolute;
    margin: 0;
    white-space: nowrap;
    line-height: 1;
  }
  .headline-question {
    left: 37px; top: 28px;
    font-size: 70px;
    color: var(--praxis-blau);
    letter-spacing: 1px;
  }
  .headline-answer {
    left: 414px; top: 37px;
    font-size: 53px;
    color: var(--weiss);
  }
  .appointment-label {
    left: 82px; top: 374px;
    font-size: 32px;
    line-height: 40px;
    color: var(--weiss);
  }
  .appointment-fields {
    left: 417px; top: 374px;
    font-size: 32px;
    line-height: 40px;
    color: var(--praxis-blau);
  }
  .voucher-title {
    left: 37px; top: 58px;
    font-size: 76px;
    color: var(--weiss);
  }
  .voucher-subject {
    left: 37px; top: 190px;
    font-size: 49px;
    line-height: 56px;
    color: var(--weiss);
  }
  .voucher-redeem {
    left: 0; width: 741px; top: 392px;
    font-size: 24px;
    line-height: 30px;
    text-align: center;
    color: var(--weiss);
  }
</style>
</head>
<body>

<section class="card card--front" aria-label="Vorderseite Terminkarte">
  <svg class="card-shapes" viewBox="0 0 741 480" xmlns="http://www.w3.org/2000/svg">
    <defs>
      <linearGradient id="portrait-senior-woman" x1="0" y1="0" x2="0" y2="1">
        <stop offset="0" stop-color="#cbbfb2"/><stop offset="1" stop-color="#a9bfbd"/>
      </linearGradient>
      <linearGradient id="portrait-teen" x1="0" y1="0" x2="0" y2="1">
        <stop offset="0" stop-color="#dcdcdc"/><stop offset="1" stop-color="#4a607c"/>
      </linearGradient>
      <linearGradient id="portrait-senior-man" x1="0" y1="0" x2="0" y2="1">
        <stop offset="0" stop-color="#9fb6bd"/><stop offset="1" stop-color="#c9c6c1"/>
      </linearGradient>
      <linearGradient id="portrait-young-woman" x1="0" y1="0" x2="0" y2="1">
        <stop offset="0" stop-color="#e2e2e0"/><stop offset="1" stop-color="#8a8f95"/>
      </linearGradient>
    </defs>
    <polygon class="band-top" points="397,0 741,0 741,114 388,114" fill="var(--praxis-blau)"/>
    <g class="portrait-strip">
      <polygon points="0,114 201,114 183,345 0,345" fill="url(#portrait-senior-woman)" role="img" aria-label="Foto: lachende Seniorin mit erhobenen Daumen"/>
      <polygon points="201,114 386,114 368,345 183,345" fill="url(#portrait-teen)" role="img" aria-label="Foto: lächelnder Jugendlicher mit verschränkten Armen"/>
      <polygon points="386,114 572,114 553,345 368,345" fill="url(#portrait-senior-man)" role="img" aria-label="Foto: lachender älterer Herr mit grauem Bart"/>
      <polygon points="572,114 741,114 741,345 553,345" fill="url(#portrait-young-woman)" role="img" aria-label="Foto: jubelnde junge Frau"/>
    </g>
    <polygon class="band-bottom" points="0,345 366,345 356,480 0,480" fill="var(--praxis-blau)"/>
  </svg>
  <p class="text headline-question">WARTEN?</p>
  <p class="text headline-answer">Nicht bei uns</p>
  <p class="text appointment-label">Ihr persönlicher<br>Wunschtermin</p>
  <p class="text appointment-fields">Datum:<br>Uhrzeit:</p>
</section>

<section class="card card--back" aria-label="Rückseite Gutschein">
  <svg class="card-shapes" viewBox="0 0 741 480" xmlns="http://www.w3.org/2000/svg">
    <defs>
      <linearGradient id="coffee-photo" x1="0" y1="0" x2="0.6" y2="1">
        <stop offset="0" stop-color="#6e5e52"/>
        <stop offset="0.5" stop-color="#8a6a52"/>
        <stop offset="1" stop-color="#3a2418"/>
      </linearGradient>
    </defs>
    <polygon points="423,0 741,0 741,371 393,371" fill="url(#coffee-photo)" role="img" aria-label="Foto: dampfende Kaffeetasse mit Kaffeebohnen und Kaffeemühle"/>
  </svg>
  <p class="text voucher-title">Gutschein</p>
  <p class="text voucher-subject">für eine<br>Kaffespezialität</p>
  <p class="text voucher-redeem">Einzulösen in der Hausarztpraxis<br>Martin Weidenau • 04319 Lindenau-Feldrain</p>
</section>

</body>
</html>
```